Company or website name
- Veltrano
- Links to the website
- http://mpbjuristes.ca/
- Describe your company and organization and target audience
- Company secretarial and management for small business.
- The design should have the following
- The model should include :  - 5 pages. - Clean and modern design. - You must use the images are joined and make a mixture between the model of the website to respect and incorporate photos.
- Other Facts

```html
<!DOCTYPE html>
<html lang="en">
<head>
<meta charset="utf-8">
<title>Veltrano — Company Secretarial Management</title>
<link href="https://fonts.googleapis.com/css2?family=Jost:wght@400;500;600&family=Roboto:wght@400;500;700&family=Open+Sans:wght@400;600;700&display=swap" rel="stylesheet">
<style>
:root{
  --blue:#0d4f9c;
  --blue-dark:#0f2c5c;
  --blue-deeper:#0a2350;
  --red:#c0202a;
  --red-deep:#b31b23;
  --grey-bg:#efefef;
  --text:#444;
  --white:#fff;
}
*{margin:0;padding:0;box-sizing:border-box}
html,body{width:786px;height:1200px;overflow:hidden;background:var(--white)}
body{position:relative;font-family:"Open Sans",sans-serif;color:var(--text)}
.abs{position:absolute}

/* header */
.brand{left:118px;top:12px;font-family:"Roboto",sans-serif;font-weight:500;font-size:28px;color:var(--blue);letter-spacing:.5px}
.phone-badge{left:552px;top:14px;width:122px;height:24px;background:var(--red);display:flex;align-items:center;border-radius:2px;overflow:hidden}
.phone-badge .ico{width:24px;height:24px;background:var(--blue);display:flex;align-items:center;justify-content:center}
.phone-badge span{font-family:"Roboto",sans-serif;font-weight:500;color:var(--white);font-size:13.5px;padding-left:6px}

/* nav */
.main-nav{left:0;top:54px;width:786px;height:29px;background:var(--blue)}
.nav-item{top:0;height:29px;line-height:29px;font-family:"Open Sans",sans-serif;font-weight:700;font-size:8.5px;color:var(--white);transform:translateX(-50%);white-space:nowrap}
.nav-active{left:118px;top:0;width:98px;height:29px;background:var(--red)}

/* hero */
.hero-photo{left:0;top:83px;width:786px;height:293px;background:linear-gradient(100deg,#0e3f7c 0%,#1a5596 45%,#0e3c74 60%,#242a33 72%,#1b2f4f 85%,#0f4686 100%)}
.hero-title{left:126px;top:167px;font-family:"Jost",sans-serif;font-weight:500;font-size:30px;line-height:28px;color:var(--white)}
.hero-sub{left:124px;top:271px;font-family:"Jost",sans-serif;font-size:13px;line-height:16.5px;color:var(--white)}
.hero-arrow{top:206px}

/* welcome */
.welcome-title{left:0;top:417px;width:786px;text-align:center;font-family:"Jost",sans-serif;font-weight:600;font-size:17px;letter-spacing:2.5px;color:var(--blue-dark)}
.welcome-title em,.value-title em{font-style:normal;color:var(--red)}
.welcome-text{left:120px;top:450px;width:546px;text-align:center;font-size:9.6px;line-height:13.7px;color:#555}

/* value */
.value-band{left:0;top:563px;width:786px;height:244px;background:var(--grey-bg);border-top:1px solid #ddd;border-bottom:1px solid #ddd}
.value-title{left:0;top:586px;width:786px;text-align:center;font-family:"Roboto",sans-serif;font-weight:500;font-size:16px;color:var(--blue)}
.value-circle{top:624px;width:113px;height:113px;border-radius:50%;background:var(--blue);display:flex;align-items:center;justify-content:center}
.value-circle.accent{background:var(--red-deep)}
.value-label{top:748px;width:160px;text-align:center;font-family:"Roboto",sans-serif;font-size:11.3px;line-height:13.6px;color:var(--blue)}

/* testimonials */
.quote-card{top:849px;width:264px;height:94px;background:linear-gradient(#fff,#f5f5f5);border:1px solid #e2e2e2;border-radius:2px}
.quote-card p{padding:15px 16px 0 17px;font-size:8.6px;line-height:12px;color:#666}
.quote-card .bar{position:absolute;right:7px;bottom:-1px;width:150px;height:2px;background:var(--blue)}
.quote-card .tail{position:absolute;left:80px;bottom:-11px}
.avatar{top:949px;width:30px;height:30px;background:linear-gradient(#c9b8ac,#8a7b70)}
.author{top:961px;font-family:"Open Sans",sans-serif;font-weight:700;font-size:7.6px;color:var(--blue-dark)}

/* footer */
.footer-rule{left:0;top:1024px;width:786px;height:3px;background:var(--red)}
.footer-band{left:0;top:1027px;width:786px;height:143px;background:var(--blue-dark)}
.footer-map{left:409px;top:1027px;width:377px;height:143px;background:linear-gradient(135deg,#e9e9e9,#d6d6d6);clip-path:polygon(0 0,100% 0,100% 100%,86px 100%)}
.pin-box{left:118px;top:1027px;width:39px;height:42px;background:var(--red);display:flex;align-items:center;justify-content:center}
.reach-title{left:167px;top:1037px;font-family:"Roboto",sans-serif;font-weight:500;font-size:12px;color:var(--white)}
.reach-line{left:169px;font-family:"Open Sans",sans-serif;font-weight:600;font-size:8px;color:var(--white);display:flex;align-items:center;gap:6px}
.bottom-bar{left:0;top:1170px;width:786px;height:30px;background:var(--blue-deeper)}
.copyright{left:118px;top:1179px;font-size:8.2px;color:var(--white)}
.social{top:1175px;width:19px;height:19px;border:1.2px solid var(--white);border-radius:50%}
</style>
</head>
<body>

<header>
  <div class="abs brand">Veltrano</div>
  <div class="abs phone-badge">
    <div class="ico">
      <svg width="13" height="10" viewBox="0 0 13 10"><path d="M1 3c3-3 8-3 11 0v2H9V3.5c-2-.7-3-.7-5 0V5H1z" fill="#fff"/><rect x="3" y="5" width="7" height="4.5" rx="1" fill="#fff"/></svg>
    </div>
    <span>123-4567-890</span>
  </div>
</header>

<nav class="abs main-nav">
  <div class="abs nav-active"></div>
  <div class="abs nav-item" style="left:167px">COMPANY</div>
  <div class="abs nav-item" style="left:281px">INCORPORATION</div>
  <div class="abs nav-item" style="left:401px">ACCOUNTING</div>
  <div class="abs nav-item" style="left:512px">INVESTMENT</div>
  <div class="abs nav-item" style="left:619px">CONTACT</div>
</nav>

<section>
  <div class="abs hero-photo" role="img" aria-label="Photo of a smiling young man in a dark jacket in front of a blue-toned city skyline"></div>
  <h1 class="abs hero-title">SIMPLE<br>COMPANY SECRETARIAL<br>MANAGEMENT</h1>
  <p class="abs hero-sub">We establish and administer all forms of onshore and offshore<br>vehicles, including companies, partnerships and trusts.</p>
  <svg class="abs hero-arrow" style="left:95px" width="10" height="16" viewBox="0 0 10 16"><path d="M8 2 2 8l6 6" stroke="#fff" stroke-width="2.2" fill="none"/></svg>
  <svg class="abs hero-arrow" style="left:681px" width="10" height="16" viewBox="0 0 10 16"><path d="m2 2 6 6-6 6" stroke="#fff" stroke-width="2.2" fill="none"/></svg>
</section>

<section>
  <h2 class="abs welcome-title">WELCOME TO <em>VELTRANO</em></h2>
  <p class="abs welcome-text">Lorem ipsum dolor sit amet, consectetur adipiscing elit. Quis est, qui non oderit libidinosam, protervam adolescentiam? Quid igitur dubitamus in tota eius natura quaerere quid sit effectum? Vitae autem degendae ratio maxime quidem illis placuit quieta. Terram, mihi crede, ea lanx et maria deprimet. Si qua in iis corrigere voluit, deteriora fecit. Duo Reges: constructio interrete. Iam in altera philosophiae parte.<br>Qua tu etiam inprudens utebare non numquam.</p>
</section>

<section>
  <div class="abs value-band"></div>
  <h2 class="abs value-title">HOW WE DELIVER <em>VALUE</em></h2>

  <div class="abs value-circle accent" style="left:115px">
    <svg width="56" height="50" viewBox="0 0 56 50" fill="none" stroke="#fff" stroke-width="2"><circle cx="27" cy="6" r="3.5"/><path d="M27 10v6M42 4v40M36 26h16M4 20h26M4 40c8-2 10-12 20-10s8 14 18-4"/><circle cx="42" cy="26" r="3" fill="#fff"/><circle cx="22" cy="42" r="3"/></svg>
  </div>
  <div class="abs value-circle" style="left:260px">
    <svg width="46" height="52" viewBox="0 0 46 52" fill="none" stroke="#fff" stroke-width="2"><rect x="4" y="2" width="32" height="42"/><path d="M40 8v42H10"/><path d="M10 10h22M10 16h22"/><path d="M10 34l7-8 6 5 8-9" /></svg>
  </div>
  <div class="abs value-circle" style="left:408px">
    <svg width="44" height="44" viewBox="0 0 44 44" fill="#fff"><rect x="2" y="6" width="10" height="10"/><rect x="14" y="6" width="10" height="10"/><rect x="27" y="2" width="11" height="11" transform="rotate(15 32 8)"/><rect x="2" y="18" width="10" height="10"/><rect x="14" y="18" width="10" height="10"/><rect x="28" y="18" width="10" height="10" transform="rotate(-20 33 23)"/><rect x="2" y="30" width="10" height="10"/><rect x="14" y="30" width="10" height="10"/></svg>
  </div>
  <div class="abs value-circle" style="left:560px">
    <svg width="52" height="48" viewBox="0 0 52 48" fill="none" stroke="#fff" stroke-width="2.4"><rect x="3" y="20" width="9" height="25" fill="#fff"/><path d="M16 22c6-4 10-10 10-18 5 0 7 5 5 14h14c3 0 4 3 2 5 2 1 2 4 0 5 2 1 2 4-1 5 1 2 0 5-3 5H16z"/></svg>
  </div>

  <div class="abs value-label" style="left:91px">Entity formation and<br>establishment</div>
  <div class="abs value-label" style="left:237px">Annual compliance and<br>statutory maintenance</div>
  <div class="abs value-label" style="left:385px">Corporate Restructuring<br>and entity rationalisation</div>
  <div class="abs value-label" style="left:537px">Best practices and<br>corporate governance</div>
</section>

<section>
  <div class="abs quote-card" style="left:118px">
    <p>Lorem ipsum dolor sit amet, no oporteat vituperata sit, eum assum causae vulputate in. Cu commune inimicus qui, eos in choro antiopam cotidieque. Ei vel possit efficiendi. His sale autem prompta et, vis nullam adipisci et, nam ei mucius viderer platonem.</p>
    <div class="bar"></div>
    <svg class="tail" width="26" height="12" viewBox="0 0 26 12"><path d="M0 0h26L2 11z" fill="#f5f5f5" stroke="#e2e2e2"/><path d="M1 -1h24" stroke="#f5f5f5" stroke-width="2"/></svg>
  </div>
  <div class="abs avatar" style="left:118px" role="img" aria-label="Portrait photo of a client"></div>
  <div class="abs author" style="left:152px">Marin Toles</div>

  <div class="abs quote-card" style="left:405px">
    <p>Lorem ipsum dolor sit amet, no oporteat vituperata sit, eum assum causae vulputate in. Cu commune inimicus qui, eos in choro antiopam cotidieque. Ei vel possit efficiendi. His sale autem prompta et, vis nullam adipisci et, nam ei mucius viderer platonem.</p>
    <div class="bar"></div>
    <svg class="tail" width="26" height="12" viewBox="0 0 26 12"><path d="M0 0h26L2 11z" fill="#f5f5f5" stroke="#e2e2e2"/><path d="M1 -1h24" stroke="#f5f5f5" stroke-width="2"/></svg>
  </div>
  <div class="abs avatar" style="left:405px" role="img" aria-label="Portrait photo of a client"></div>
  <div class="abs author" style="left:439px">Marin Toles</div>
</section>

<footer>
  <div class="abs footer-rule"></div>
  <div class="abs footer-band"></div>
  <div class="abs footer-map" role="img" aria-label="Street map showing the office location"></div>
  <div class="abs pin-box">
    <svg width="16" height="22" viewBox="0 0 16 22" fill="none" stroke="#fff" stroke-width="1.6"><path d="M8 21C3 14 1 11 1 8a7 7 0 0 1 14 0c0 3-2 6-7 13z"/><circle cx="8" cy="8" r="3"/></svg>
  </div>
  <div class="abs reach-title">REACH US</div>
  <div class="abs reach-line" style="top:1074px">xxxxxxxxxxxxxxxxxxxxxxxxx</div>
  <div class="abs reach-line" style="top:1088px">xxxxxxxxxxxxxxxxxx</div>
  <div class="abs reach-line" style="top:1102px">
    <svg width="9" height="7" viewBox="0 0 13 10"><path d="M1 3c3-3 8-3 11 0v2H9V3.5c-2-.7-3-.7-5 0V5H1z" fill="#fff"/><rect x="3" y="5" width="7" height="4.5" rx="1" fill="#fff"/></svg>123-456-7890
  </div>
  <div class="abs reach-line" style="top:1116px">
    <svg width="9" height="7" viewBox="0 0 9 7"><rect width="9" height="7" fill="#fff"/><path d="M0 0l4.5 4L9 0" stroke="#0f2c5c" fill="none"/></svg>info@veltrano.com
  </div>

  <div class="abs bottom-bar"></div>
  <div class="abs copyright">Copyright 2016. All rights reserved.</div>
  <div class="abs social" style="left:586px" aria-label="Social link"></div>
  <div class="abs social" style="left:617px" aria-label="Social link"></div>
  <div class="abs social" style="left:647px" aria-label="Social link"></div>
</footer>

</body>
</html>
```